Website design for commercial and residential security company

we're looking to see some new designs for an established company with no website.

homepage and one inner page

here is a link to the homepage content, sitemap, logo and more.
https://files.brontavel.net/share/7QxmPzLrTw2vNkdJhYcsa9eFgbUoiVwRn?view=open

call to action should be Request A Quote

if you have any questions please send them to us asap

thank you

1 page

Sans Serif

```html
<!DOCTYPE html>
<html lang="en">
<head>
<meta charset="utf-8">
<title>Beacon Point – Security Services</title>
<link href="https://fonts.googleapis.com/css2?family=Oswald:wght@300;400;500;600&family=Hind:wght@400;500;600&display=swap" rel="stylesheet">
<style>
:root{
  --gold:#cfab2f;
  --gold-dark:#b8961f;
  --ink:#2b2b2b;
  --text:#555;
  --grey:#676767;
  --light:#f4f4f4;
  --footer:#3b3b3b;
  --white:#fff;
}
*{box-sizing:border-box;margin:0;padding:0}
html,body{width:1200px;height:5277px;overflow:hidden}
body{font-family:'Hind',sans-serif;color:var(--text);background:var(--white);position:relative}
.abs{position:absolute}
h1,h2,h3,h4{font-family:'Oswald',sans-serif;font-weight:500;color:var(--ink)}
.eyebrow{font-size:10px;letter-spacing:.5px;color:var(--gold);text-transform:uppercase}
.body{font-size:11px;line-height:22px}
.btn{display:inline-block;font-family:'Oswald',sans-serif;font-size:11px;font-weight:500;color:#fff;text-transform:uppercase;text-align:center;letter-spacing:.3px}
.ph{position:absolute;overflow:hidden}
/* top bar */
.topbar{top:0;left:0;width:1200px;height:37px;font-size:9px;color:#444}
.topbar span{position:absolute;top:13px}
.social{position:absolute;top:9px;width:16px;height:16px;background:#bbb;border-radius:2px}
/* header */
.header{top:37px;left:0;width:1200px;height:88px;background:#fff;border-bottom:1px solid #eee}
.logo{position:absolute;left:164px;top:30px;display:flex;align-items:center;gap:8px}
.logo .mark{width:18px;height:18px;background:var(--gold)}
.logo b{font-family:'Oswald',sans-serif;font-weight:500;font-size:22px;color:var(--gold);letter-spacing:.5px}
.nav{position:absolute;left:492px;top:37px;display:flex;gap:26px;font-family:'Oswald',sans-serif;font-size:11px;color:#333}
.nav .on{color:var(--gold);border-bottom:1px solid var(--gold)}
.quote{position:absolute;right:0;top:0;width:213px;height:88px;background:var(--gold);color:#fff;font-family:'Oswald',sans-serif;font-weight:500;font-size:12px;display:flex;align-items:center;justify-content:center}
/* hero */
.hero{top:125px;left:0;width:1200px;height:711px;background:
  radial-gradient(ellipse 260px 200px at 150px 170px,#2e2e2e,transparent 70%),
  radial-gradient(ellipse 380px 260px at 880px 260px,#4a4a4a,transparent 75%),
  radial-gradient(ellipse 300px 220px at 420px 120px,#f0f0f0,transparent 70%),
  linear-gradient(135deg,#a6a6a6,#d9d9d9 45%,#8c8c8c)}
.hero-text{position:absolute;top:222px;width:1200px;text-align:center}
.hero-text .w{color:#fff;font-size:12px;letter-spacing:3px}
.hero-text h1{color:var(--gold);font-size:58px;line-height:66px;font-weight:600;margin-top:8px;text-shadow:0 2px 4px rgba(0,0,0,.35)}
.hero-text h2{color:#fff;font-size:36px;line-height:42px;font-weight:500;text-shadow:0 2px 4px rgba(0,0,0,.35)}
.hero .btn{position:absolute;left:539px;top:416px;width:122px;height:45px;line-height:41px;background:#555;border:2px solid #aaa}
/* service cards */
.cards{top:713px;left:162px;width:876px;height:245px;background:#fff;box-shadow:0 4px 14px rgba(0,0,0,.1)}
.card-photo{position:absolute;top:6px;height:233px}
.card-photo span{position:absolute;bottom:18px;width:100%;text-align:center;font-family:'Oswald',sans-serif;color:#fff;font-size:15px}
.card-gold{position:absolute;left:600px;top:0;width:276px;height:245px;background:var(--gold);padding:8px}
.card-gold div{border:1px solid rgba(255,255,255,.7);height:100%;padding:62px 30px 0 30px;font-family:'Oswald',sans-serif;color:#fff;font-size:25px;line-height:34px}
/* cctv */
.cctv-text{top:1024px;left:162px;width:370px}
.cctv-text h2{font-size:28px;margin:4px 0 18px}
.list{display:grid;grid-template-columns:165px 205px;gap:12px 0;margin:14px 0;font-size:11px;white-space:nowrap}
.list span::before{content:"";display:inline-block;width:12px;height:12px;background:var(--gold);margin-right:12px;vertical-align:-2px}
.cctv-text .btn{background:var(--grey);width:120px;height:46px;line-height:46px;margin-top:22px}
.monitor-badge{top:1160px;left:764px;width:122px;height:122px;border-radius:50%;background:var(--gold);border:5px solid #fff;color:#fff;font-family:'Oswald',sans-serif;font-size:13px;line-height:20px;text-align:center;padding-top:26px}
/* features */
.features{top:1505px;left:0;width:1200px;height:471px;background:var(--light)}
.feat{position:absolute;width:220px}
.feat .ic{width:58px;height:58px;background:var(--gold);display:flex;align-items:center;justify-content:center;float:left;margin-right:20px}
.feat h3{font-size:18px;font-weight:400;line-height:58px}
.feat p{clear:both;font-size:10.5px;line-height:22px;padding-top:12px}
/* products */
.section-head{position:absolute;left:0;width:1200px;text-align:center}
.section-head h2{font-size:29px;margin-top:4px}
.prod{position:absolute;top:2132px;width:203px;text-align:center}
.prod .img{height:240px;border:1px solid #e6e6e6;background:#f5f5f5}
.prod h4{font-size:16px;font-weight:300;margin-top:28px}
.prod p{font-size:10.5px;line-height:21px;margin-top:10px}
.prod .btn{width:123px;height:46px;line-height:46px;background:var(--grey);margin-top:20px}
.prod .btn.g{background:var(--gold)}
.arrow{position:absolute;top:2242px}
/* split sections */
.split-text{position:absolute;width:360px}
.split-text h2{font-size:28px;margin:4px 0 20px}
.split-text p{font-size:10.5px;line-height:22px;margin-bottom:14px;color:#f1f1f1}
.split-text .btn{width:122px;height:46px;line-height:46px;margin-top:20px}
/* recent work */
.filters{position:absolute;top:3712px;left:0;width:1200px;text-align:center;font-family:'Oswald',sans-serif;font-size:11px;color:#444}
.filters span{margin:0 10px}
.filters .on{color:var(--gold);border-bottom:1px solid var(--gold)}
.tile{position:absolute;width:278px;height:262px}
/* why */
.why{top:4383px;left:0;width:1200px;height:512px;background:#fff}
.acc{border-bottom:1px solid #e4e4e4;padding:12px 0;font-family:'Oswald',sans-serif;font-weight:400;font-size:15px;color:#444;position:relative}
.acc::after{content:"+";position:absolute;right:0;top:10px;color:#999;font-family:'Hind',sans-serif;font-size:18px}
.acc.open{color:var(--gold);border:0;padding-bottom:6px}
.acc.open::after{content:"–";color:var(--gold)}
/* footer */
.footer{top:4895px;left:0;width:1200px;height:337px;background:var(--footer);color:#ddd}
.footer h4{color:#fff;font-size:19px;font-weight:400;margin-bottom:26px}
.fcol{position:absolute;top:70px;font-size:10.5px;line-height:31px}
.copy{top:5232px;left:0;width:1200px;height:45px;background:var(--gold);color:#fff;font-size:10px;text-align:center;line-height:45px}
</style>
</head>
<body>

<div class="abs topbar">
  <svg class="abs" style="left:162px;top:13px" width="9" height="9" viewBox="0 0 10 10"><path d="M2 1l2 2-1 1.5c.7 1.3 1.6 2.2 2.6 2.6L7 6l2 2-1.5 1.5C4 9 1 6 .5 2.5z" fill="#444"/></svg>
  <span style="left:176px">(555) 014-2290</span>
  <svg class="abs" style="left:268px;top:13px" width="10" height="8" viewBox="0 0 10 8"><rect width="10" height="8" fill="#444"/><path d="M0 0l5 4 5-4" stroke="#fff" fill="none"/></svg>
  <span style="left:284px">hello@beaconpoint-mail.com</span>
  <i class="social" style="left:962px"></i><i class="social" style="left:988px"></i><i class="social" style="left:1014px"></i>
</div>

<header class="abs header">
  <div class="logo"><i class="mark"></i><b>BEACON POINT</b></div>
  <nav class="nav"><span class="on">HOME</span><span>ABOUT</span><span>SOLUTIONS ⌄</span><span>RESOURCES ⌄</span><span>CONTACT</span></nav>
  <div class="quote">REQUEST A FREE QUOTE</div>
</header>

<section class="abs hero" role="img" aria-label="Hands holding a tablet showing a camera feed over dome security cameras and building plans">
  <div class="hero-text">
    <div class="w">WELCOME TO BEACON POINT</div>
    <h1>Security service</h1>
    <h2>for your personal safety</h2>
  </div>
  <span class="btn">GET STARTED</span>
</section>

<div class="abs cards">
  <div class="card-photo" style="left:6px;width:291px;background:radial-gradient(ellipse 70px 90px at 50% 45%,#e6e6e6,transparent 80%),linear-gradient(180deg,#9fb3c4,#5b6d7c 60%,#2f3a44)" role="img" aria-label="Dome camera in an industrial plant"><span>Commercial Services</span></div>
  <div class="card-photo" style="left:303px;width:291px;background:radial-gradient(ellipse 90px 60px at 35% 55%,#e7c27a,transparent 80%),linear-gradient(180deg,#7a7d86,#3a3b40 70%,#1f1f22)" role="img" aria-label="House at dusk behind a security camera"><span>Residential Services</span></div>
  <div class="card-gold"><div>Your Most Trusted Partner in Monitoring!</div></div>
</div>

<div class="abs cctv-text">
  <div class="eyebrow">Our Monitoring Services</div>
  <h2>CCTV for your Safety</h2>
  <p class="body">Lorem ipsum dolor sit amet, consectetur adipiscing elit, sed doran tempor incididunt ut labore et dolore magna aliqua. Ut enim adedtile minim veniam, quis nostrud exercitation ullamco laboris nisi ut est aliquip ex ea commodo consequat:</p>
  <div class="list"><span>Consectetur adipiscing</span><span>Consectetur adipiscing elet mor</span><span>Consectetur adipiscing</span><span>Consectetur adipiscing elet mor</span></div>
  <p class="body">Lorem ipsum dolor sit amet, consectetur adipiscing elit, sed doran tempor incididunt ut labore et dolore magna aliqua. Lorem ipsum dolor sit amet, consectetur adipiscing elit, sed doran tempor turest adipiscing elit, sed doran tempor incididunt ut labore et dolore</p>
  <span class="btn">LEARN MORE</span>
</div>
<div class="ph" style="left:610px;top:1028px;width:208px;height:172px;background:radial-gradient(ellipse 50px 40px at 45% 55%,#3a3a3a,transparent 80%),linear-gradient(135deg,#f2f2f2,#cfcfcf 60%,#a9a9a9)" role="img" aria-label="Assorted security cameras on a white surface"></div>
<div class="ph" style="left:830px;top:1028px;width:208px;height:172px;background:radial-gradient(ellipse 50px 70px at 45% 75%,#6c8fb8,transparent 80%),linear-gradient(135deg,#f6f7f8,#dfe3e7)" role="img" aria-label="Technician installing a ceiling camera"></div>
<div class="ph" style="left:610px;top:1212px;width:428px;height:224px;background:radial-gradient(ellipse 90px 70px at 60% 65%,#3d3d3d,transparent 80%),radial-gradient(ellipse 80px 60px at 85% 80%,#b48e74,transparent 80%),linear-gradient(135deg,#e4e4e4,#bdbdbd)" role="img" aria-label="Hand holding a phone showing a camera feed below a dome camera"></div>
<div class="abs monitor-badge">WE MONITOR<br>WHAT MATTERS<br>THE MOST</div>

<section class="abs features">
  <div class="ph" style="left:0;top:0;width:573px;height:471px;background:radial-gradient(ellipse 200px 130px at 290px 200px,#e6dccb,transparent 75%),linear-gradient(90deg,#5f86b3 0,#a9c0d8 22%,#ececec 40%,#f4f4f4)" role="img" aria-label="White bullet security camera mounted on a wall"></div>
  <div class="feat" style="left:573px;top:72px"><div class="ic"><svg width="28" height="20" viewBox="0 0 28 20"><rect x="1" y="1" width="26" height="6" fill="none" stroke="#fff" stroke-width="2"/><circle cx="14" cy="13" r="6" fill="none" stroke="#fff" stroke-width="2"/><circle cx="14" cy="13" r="2" fill="#fff"/></svg></div><h3>Our Target</h3><p>20% increase in sales in 6 months, and some other text filler that has been used for design purposes only</p></div>
  <div class="feat" style="left:836px;top:72px"><div class="ic"><svg width="28" height="20" viewBox="0 0 28 20"><rect x="1" y="1" width="26" height="6" fill="none" stroke="#fff" stroke-width="2"/><circle cx="14" cy="13" r="6" fill="none" stroke="#fff" stroke-width="2"/><circle cx="14" cy="13" r="2" fill="#fff"/></svg></div><h3>Our Mission</h3><p>Increase search traffic this year to generate more leads, leading to larger customer base</p></div>
  <div class="feat" style="left:573px;top:270px"><div class="ic"><svg width="28" height="20" viewBox="0 0 28 20"><rect x="1" y="1" width="26" height="6" fill="none" stroke="#fff" stroke-width="2"/><circle cx="14" cy="13" r="6" fill="none" stroke="#fff" stroke-width="2"/><circle cx="14" cy="13" r="2" fill="#fff"/></svg></div><h3>Our Goals</h3><p>20-30% increase in customers that we provide monitoring for - leads to the Recurring Monthly Revenue</p></div>
  <div class="feat" style="left:836px;top:270px"><div class="ic"><svg width="28" height="20" viewBox="0 0 28 20"><rect x="1" y="1" width="26" height="6" fill="none" stroke="#fff" stroke-width="2"/><circle cx="14" cy="13" r="6" fill="none" stroke="#fff" stroke-width="2"/><circle cx="14" cy="13" r="2" fill="#fff"/></svg></div><h3>Our Milestone</h3><p>Another snippet or text filler that has been used for design purposes only and fill the empty spaces</p></div>
</section>

<div class="section-head" style="top:2040px"><div class="eyebrow">Product Information</div><h2>Our Products</h2></div>
<svg class="arrow" style="left:146px" width="24" height="12" viewBox="0 0 24 12"><path d="M23 6H2M7 1L2 6l5 5" stroke="#999" fill="none"/></svg>
<svg class="arrow" style="left:1028px" width="24" height="12" viewBox="0 0 24 12"><path d="M1 6h21M17 1l5 5-5 5" stroke="#cfab2f" fill="none"/></svg>
<div class="prod" style="left:162px"><div class="img" role="img" aria-label="White dome security camera" style="background:radial-gradient(circle 55px at 50% 50%,#e9e9e9,#c9c9c9 60%,transparent 62%),#f5f5f5"></div><h4>360 Security Camera</h4><p>Lorem ipsum dolor sit amet,seadcing elit, sed do eiusmod tempor incidid...</p><span class="btn">PRODUCT INFO</span></div>
<div class="prod" style="left:385px"><div class="img" role="img" aria-label="Bullet camera on a wall bracket" style="background:radial-gradient(ellipse 60px 40px at 55% 45%,#8a8a8a,#d6d6d6 60%,transparent 62%),#f5f5f5"></div><h4>Camera One</h4><p>Lorem ipsum dolor sit amet,seadcing elit, sed do eiusmod tempor incidid...</p><span class="btn g">PRODUCT INFO</span></div>
<div class="prod" style="left:610px"><div class="img" role="img" aria-label="Black bullet security camera" style="background:radial-gradient(ellipse 60px 40px at 55% 45%,#1e1e1e,#3c3c3c 60%,transparent 62%),#f5f5f5"></div><h4>Camera Two</h4><p>Lorem ipsum dolor sit amet,seadcing elit, sed do eiusmod tempor incidid...</p><span class="btn">PRODUCT INFO</span></div>
<div class="prod" style="left:834px"><div class="img" role="img" aria-label="White outdoor bullet camera" style="background:radial-gradient(ellipse 60px 40px at 45% 55%,#e4e4e4,#9a9a9a 60%,transparent 62%),#f5f5f5"></div><h4>Camera Three</h4><p>Lorem ipsum dolor sit amet,seadcing elit, sed do eiusmod tempor incidid...</p><span class="btn">PRODUCT INFO</span></div>

<div class="ph" style="left:0;top:2621px;width:600px;height:472px;background:var(--grey)"></div>
<div class="split-text" style="left:162px;top:2688px">
  <div class="eyebrow">What we offer?</div>
  <h2 style="color:#fff">Commercial Services</h2>
  <p>We specialize in implementation of CCTV, Access Control, Alarm, Audio systems for small and large businesses.</p>
  <p>Commercial/residential customers (various ages) looking to secure their businesses/homes with our integrated systems. We are looking to provide installation, service and monitoring for these customers.</p>
  <p>Lorem ipsum dolor sit amet, consectetur adipiscing elit, sed domod tempor incididunt ut labore et dolore magna aliqua.</p>
  <span class="btn" style="background:var(--gold)">LEARN MORE</span>
</div>
<div class="ph" style="left:600px;top:2621px;width:600px;height:472px;background:radial-gradient(ellipse 180px 150px at 200px 260px,#8a6a55,transparent 75%),radial-gradient(circle 70px at 515px 160px,#f7f7f7,transparent 90%),linear-gradient(90deg,#8c8983,#c9c5bd 45%,#e6e4e0 75%,#f0efec)" role="img" aria-label="Family on a sofa beside a wall thermostat"></div>

<div class="ph" style="left:0;top:3093px;width:600px;height:475px;background:radial-gradient(ellipse 150px 200px at 490px 230px,#e8e8e8,transparent 75%),linear-gradient(90deg,#8a7440,#c9a94e 30%,#d9cfb4 55%,#f2f2f2 80%)" role="img" aria-label="Operator on the phone in front of security monitors"></div>
<div class="ph" style="left:600px;top:3093px;width:600px;height:475px;background:var(--gold)"></div>
<div class="split-text" style="left:687px;top:3158px">
  <div class="eyebrow" style="color:#fff">What we offer?</div>
  <h2 style="color:#fff">Residential Services</h2>
  <p>We specialize in CCTV, Alarm, automation, A/V and networking for residential homes.</p>
  <p>Business owners are ideal, especially when they have multiple business locations. We can generate more recurring the monthly revenue from monitoring their systems.</p>
  <p>Lorem ipsum dolor sit amet, consectetur adipiscing elit, sed domod tempor incididunt ut labore et dolore magna aliqua.</p>
  <span class="btn" style="background:var(--grey)">LEARN MORE</span>
</div>

<div class="section-head" style="top:3630px"><div class="eyebrow">Project Showcase</div><h2>Recent Work</h2></div>
<div class="filters"><span class="on">ALL</span><span>ALARMS</span><span>CCTV</span><span>ACCESS CONTROL</span><span>AUDIO SYSTEMS</span></div>
<div class="tile" style="left:162px;top:3764px;background:radial-gradient(ellipse 60px 50px at 55% 30%,#f2f2f2,transparent 80%),linear-gradient(135deg,#f0d27a,#e3be55 60%,#d1ab3c)" role="img" aria-label="Hands adjusting a camera on a yellow wall"></div>
<div class="tile" style="left:461px;top:3764px;background:radial-gradient(ellipse 60px 80px at 50% 80%,#3d5f8f,transparent 80%),linear-gradient(135deg,#f6f7f8,#dfe2e6)" role="img" aria-label="Technician fitting a dome camera"></div>
<div class="tile" style="left:760px;top:3764px;background:radial-gradient(ellipse 40px 60px at 60% 35%,#3a3a3a,transparent 80%),radial-gradient(ellipse 60px 60px at 45% 80%,#e0a070,transparent 80%),linear-gradient(135deg,#f3f3f3,#d9d9d9)" role="img" aria-label="Finger pressing an access keypad"></div>
<div class="tile" style="left:162px;top:4051px;background:radial-gradient(ellipse 50px 70px at 70% 45%,#3a3a3a,transparent 80%),radial-gradient(ellipse 60px 50px at 35% 65%,#d9a07c,transparent 80%),linear-gradient(135deg,#a77d58,#e9e3da 70%)" role="img" aria-label="Hand holding a card to an access reader"></div>
<div class="tile" style="left:461px;top:4051px;background:radial-gradient(ellipse 60px 80px at 30% 30%,#e8c640,transparent 80%),linear-gradient(135deg,#e4e4e4,#bdbdbd)" role="img" aria-label="Yellow cable with pliers"></div>
<div class="tile" style="left:760px;top:4051px;background:radial-gradient(ellipse 60px 60px at 75% 40%,#f4f4f4,transparent 80%),radial-gradient(ellipse 70px 70px at 30% 55%,#4d5f7a,transparent 80%),linear-gradient(135deg,#8a9ab0,#d5dbe2)" role="img" aria-label="Indoor camera watching a living room"></div>

<section class="abs why">
  <div class="ph" style="left:46px;top:70px;width:570px;height:340px;background:
    radial-gradient(ellipse 70px 40px at 300px 40px,#e8e8e8,transparent 90%),
    radial-gradient(ellipse 110px 70px at 110px 190px,#ececec,transparent 90%),
    radial-gradient(ellipse 90px 75px at 480px 150px,#3a3a3a,transparent 90%),
    radial-gradient(ellipse 90px 55px at 260px 250px,#262626,transparent 90%),
    radial-gradient(ellipse 90px 45px at 430px 265px,#2a2a2a,transparent 90%),
    #fff" role="img" aria-label="Set of white security cameras with a monitor and recorder"></div>
  <div class="abs" style="left:686px;top:60px;width:352px">
    <div class="eyebrow">What we offer?</div>
    <h2 style="font-size:28px;margin:4px 0 20px">Why Choosing Beacon Point?</h2>
    <div class="acc open">How to monitor CCTV when I am not at home?</div>
    <p style="font-size:10.5px;line-height:20px;border-bottom:1px solid #e4e4e4;padding-bottom:10px">Lorem ipsum dolor sit amet, consectetur adipiscing elit, sed domod tempor incididunt ut labore et dolore magna aliqua.</p>
    <div class="acc">Lorem ipsum dolor amet ningun postekam?</div>
    <div class="acc">Dolor amet simply text filler for design purposes?</div>
    <div class="acc">Another text filler for design purposes only?</div>
    <span class="btn" style="background:var(--gold);width:120px;height:46px;line-height:46px;margin-top:36px">FREE QUOTE</span>
  </div>
</section>

<footer class="abs footer">
  <div class="fcol" style="left:162px;width:240px">
    <div class="logo" style="position:static;margin-bottom:20px"><i class="mark"></i><b style="color:#fff">BEACON POINT</b></div>
    <p style="line-height:22px">Lorem ipsum dolor sit amet, tatura est ascing elit, setampor incididunt ut labore et dolore magna aliqua destil. Lorem simply dummy text filler est.</p>
    <div style="border-top:1px solid #555;margin-top:12px;padding-top:10px;display:flex;gap:8px"><i style="width:18px;height:18px;background:#777"></i><i style="width:18px;height:18px;background:var(--gold)"></i><i style="width:18px;height:18px;background:#777"></i></div>
  </div>
  <div class="fcol" style="left:469px"><h4>Quick Links</h4>Home<br>About<br>Solutions<br>Resources<br>Contact</div>
  <div class="fcol" style="left:675px"><h4>Sitemap</h4>Terms of Use<br>Privacy Policy<br>Careers<br>Lorem Ipsum<br>Text Filler</div>
  <div class="fcol" style="left:880px;line-height:20px"><h4>Contact Us</h4>
    <div style="display:flex;gap:14px;margin-bottom:12px"><svg width="10" height="14" viewBox="0 0 10 14"><path d="M5 0a5 5 0 015 5c0 4-5 9-5 9S0 9 0 5a5 5 0 015-5z" fill="#fff"/><circle cx="5" cy="5" r="2" fill="#3b3b3b"/></svg><span>Lorem Ipsum Street 17238,<br>Avenue 20, United States</span></div>
    <div style="display:flex;gap:14px;margin-bottom:12px"><svg width="12" height="9" viewBox="0 0 12 9"><rect width="12" height="9" fill="#fff"/><path d="M0 0l6 5 6-5" stroke="#3b3b3b" fill="none"/></svg><span>hello@beaconpoint-mail.com</span></div>
    <div style="display:flex;gap:14px"><svg width="11" height="11" viewBox="0 0 10 10"><path d="M2 1l2 2-1 1.5c.7 1.3 1.6 2.2 2.6 2.6L7 6l2 2-1.5 1.5C4 9 1 6 .5 2.5z" fill="#fff"/></svg><span>(555) 014-2290</span></div>
  </div>
</footer>
<div class="abs copy">Copyright © 2021 <b>Beacon Point Business Solutions</b> - All Rights Reserved</div>

</body>
</html>
```